SunGrove Yoga Website Design

Business Logo - attached
5 pages being:
Home
About
Classes
Blog
Contact

Would like Scrolling webpage and yoga symbols to be used.

Must have's being:
Easy to navigate, Text needs to be able to be edited/updated, Enquire Now Links, More Information Links, be a secure site, SEO,

Please refer to attached document for the information for the body of the website.

Target Market(s)

Educators, Community Service, Health and Wellbeing, Mental Health

Industry/Entity Type

Yoga

Coding

Coded - Design and coding required

Number of Pages Required

5+ page

Font styles to use
Other font styles liked:
• Bella Bold BC

Colors
0094D4
00A9DD
6FCCEA
C7EBF8
E9F6FB
6B429C
8869AF
B7A5CE
E3DAEB
F3F0F8

Requirements
Must have
• Easy to navigate, Text needs to be able to be edited/updated, Enquire Now Links, More Information Links, be a secure site, SEO,
Nice to have
• Scrolling webpage, yoga symbols

```html
<!DOCTYPE html>
<html lang="en">
<head>
<meta charset="utf-8">
<title>SunGrove Yoga</title>
<link href="https://fonts.googleapis.com/css2?family=Cormorant+Garamond:wght@500;600&family=Open+Sans:wght@400;600;700&family=Poppins:wght@500;600;700&display=swap" rel="stylesheet">
<style>
:root{
  --purple:#6b429c;
  --purple-mid:#8869af;
  --purple-soft:#b7a5ce;
  --lilac:#e3daeb;
  --lilac-pale:#f3f0f8;
  --ink:#2b2a33;
  --body:#6d6a75;
  --dark:#24252d;
  --white:#ffffff;
  --star:#f5a623;
}
*{box-sizing:border-box;margin:0;padding:0}
html,body{width:1200px;height:4520px;overflow:hidden}
body{font-family:"Open Sans",sans-serif;color:var(--body);background:var(--white);position:relative}
section,header,footer{position:absolute;left:0;width:1200px}

/* header */
.site-header{top:0;height:100px;background:var(--white);z-index:5;box-shadow:0 2px 10px rgba(0,0,0,.06)}
.contact-chip{position:absolute;top:16px;display:flex;gap:12px;align-items:center;font-size:13px}
.contact-chip .dot{width:34px;height:34px;border-radius:50%;background:var(--purple);display:flex;align-items:center;justify-content:center}
.contact-chip b{display:block;color:var(--ink);font-size:13px}
.main-nav{position:absolute;top:70px;left:120px;right:120px;display:flex;justify-content:space-between;font-size:14px;color:var(--ink)}
.main-nav .gap{width:200px}
.book-btn{position:absolute;right:120px;top:14px;background:var(--purple);color:#fff;font-size:13px;font-weight:600;padding:12px 26px;border-radius:24px}
.brand-badge{position:absolute;left:510px;top:-20px;width:180px;height:180px;border-radius:50%;background:var(--white);display:flex;flex-direction:column;align-items:center;justify-content:center;gap:8px;box-shadow:0 4px 14px rgba(0,0,0,.08)}
.brand-badge .mark{width:34px;height:34px;border-radius:50%;background:var(--purple-mid)}
.brand-badge .name{font-family:"Cormorant Garamond",serif;font-size:22px;font-weight:600;color:var(--purple)}

/* hero */
.hero{top:100px;height:760px;overflow:hidden}
.hero-photo{position:absolute;inset:0;background:linear-gradient(180deg,#6d6a66 0%,#a59486 45%,#c9a98e 70%,#8d8a92 100%)}
.hero-text{position:absolute;left:80px;top:220px;color:#fff}
.eyebrow{font-family:"Poppins",sans-serif;letter-spacing:5px;font-size:24px;font-weight:600}
.hero h1{font-family:"Poppins",sans-serif;font-size:50px;font-weight:700;margin-top:18px}
.hero p{font-size:16px;line-height:1.6;margin-top:28px;width:640px}
.btn{display:inline-block;font-size:13px;font-weight:700;padding:12px 30px;border-radius:24px;text-transform:uppercase}
.btn-purple{background:var(--purple);color:#fff}
.btn-white{background:#fff;color:var(--purple);margin-left:14px}
.hero .actions{margin-top:36px}
.hero-curve{position:absolute;left:0;bottom:0}

/* intro */
.intro{top:860px;height:640px}
.brand-art{position:absolute;left:80px;top:120px;width:440px;height:400px;display:flex;flex-direction:column;align-items:center;justify-content:center;gap:22px}
.brand-art .mark{width:220px;height:220px;border-radius:50%;background:linear-gradient(135deg,var(--lilac),var(--purple-soft))}
.brand-art .name{font-family:"Cormorant Garamond",serif;font-size:40px;font-weight:600;color:var(--purple)}
.intro-copy{position:absolute;left:620px;top:112px;width:500px}
.kicker{font-family:"Cormorant Garamond",serif;color:var(--purple-mid);font-size:20px}
.intro-copy h2{font-family:"Cormorant Garamond",serif;color:var(--ink);font-size:42px;font-weight:600;margin-top:6px}
.rule{width:500px;height:2px;background:var(--lilac);margin:18px 0 20px}
.intro-copy p{font-size:14px;line-height:1.7;margin-bottom:18px}
.intro-copy .lead{border-left:3px solid var(--purple);padding-left:14px}

/* headings */
.sec-title{position:absolute;left:0;width:1200px;text-align:center}
.sec-title h2{font-family:"Cormorant Garamond",serif;font-size:54px;font-weight:500;color:var(--purple)}
.sec-title p{font-size:14px;line-height:1.6;width:520px;margin:10px auto 0}

/* benefits */
.benefits{top:1500px;height:580px;background:var(--lilac-pale)}
.benefits .sec-title{top:60px}
.benefit-wrap{position:absolute;top:248px;width:320px;height:264px}
.benefit-card{position:absolute;left:0;top:0;width:320px;height:264px;border-radius:10px;overflow:hidden;background:linear-gradient(160deg,#8f8a90,#5b5460)}
.benefit-card h3{position:absolute;top:76px;width:100%;text-align:center;font-family:"Cormorant Garamond",serif;font-size:36px;font-weight:600;color:#fff}
.benefit-icon{position:absolute;top:-26px;left:50%;transform:translateX(-50%)}
.benefit-arrow{position:absolute;left:34px;bottom:26px}

/* why */
.why{top:2080px;height:720px}
.why .sec-title{top:58px}
.why-glow{position:absolute;left:160px;top:260px;width:880px;height:420px;border-radius:210px;background:linear-gradient(90deg,var(--lilac-pale),#fff 50%,var(--lilac-pale))}
.why-photo{position:absolute;left:390px;top:210px;width:420px;height:500px;border-radius:210px 210px 0 0;background:linear-gradient(180deg,#e9e4ef,#c8bcd6)}
.feature{position:absolute;width:260px}
.feature h4{font-family:"Cormorant Garamond",serif;font-size:25px;font-weight:600;color:var(--purple);white-space:nowrap}
.feature p{font-size:13px;line-height:1.5;margin-top:4px}
.feature.left{text-align:right}
.f-icon{position:absolute;width:74px;height:74px;border-radius:50%;background:var(--purple-soft);border:6px solid var(--lilac)}

/* hours */
.hours{top:2800px;height:580px;overflow:hidden}
.hours-photo{position:absolute;inset:0;background:linear-gradient(90deg,#2a2726 0%,#4b4039 55%,#6c5e54 100%)}
.hours-title{position:absolute;left:100px;top:150px;font-family:"Cormorant Garamond",serif;color:#fff;font-size:32px;font-weight:600}
.hours-table{position:absolute;left:100px;top:210px;width:480px;border-left:4px solid var(--purple-mid);background:rgba(0,0,0,.35)}
.hours-row{display:flex;justify-content:space-between;padding:18px 24px;color:#fff;font-size:14px;border-bottom:1px solid rgba(255,255,255,.15)}
.hours-row span:last-child{color:#d8d2de}
.appt{position:absolute;left:612px;top:152px;width:548px;height:376px;background:var(--lilac);border-radius:4px;padding:24px 28px}
.appt-head{display:flex;gap:14px;align-items:center}
.appt-head .dot{width:46px;height:46px;border-radius:50%;background:var(--purple);display:flex;align-items:center;justify-content:center}
.appt-head small{font-size:13px;color:var(--ink)}
.appt-head h3{font-family:"Cormorant Garamond",serif;font-size:36px;font-weight:600;color:var(--ink);line-height:1}
.fields{display:grid;grid-template-columns:1fr 1fr;gap:12px;margin-top:18px}
.field{background:#fff;height:40px;font-size:13px;color:var(--ink);padding:11px 14px}
.field.full{grid-column:1/3}
.submit{grid-column:1/3;background:var(--purple);color:#fff;text-align:center;font-weight:700;height:44px;line-height:44px;letter-spacing:1px}

/* reviews */
.reviews{top:3380px;height:580px}
.reviews .sec-title{top:80px}
.review{position:absolute;top:240px;width:320px;height:300px;background:#fff;box-shadow:0 6px 22px rgba(0,0,0,.1);padding:22px 24px}
.avatar{width:56px;height:56px;border-radius:50%;background:linear-gradient(135deg,var(--lilac),var(--purple-soft))}
.quote{position:absolute;right:24px;top:18px;font-family:"Cormorant Garamond",serif;font-size:90px;line-height:1;color:var(--purple-soft)}
.stars{color:var(--star);font-size:18px;letter-spacing:3px;margin-top:14px}
.review p{font-size:13px;line-height:1.55;margin-top:10px}
.review h5{font-family:"Cormorant Garamond",serif;font-size:24px;font-weight:600;color:var(--ink);margin-top:12px}
.review small{font-size:11px;color:var(--purple-mid)}

/* footer */
.site-footer{top:3960px;height:560px;background:var(--dark)}
.footer-curve{position:absolute;top:0;left:0}
.footer-brand{position:absolute;left:0;width:1200px;top:96px;display:flex;flex-direction:column;align-items:center;gap:10px}
.footer-brand .mark{width:90px;height:90px;border-radius:50%;border:3px solid var(--purple-mid)}
.footer-brand .name{font-family:"Cormorant Garamond",serif;font-size:30px;font-weight:600;color:#fff}
.footer-nav{position:absolute;top:320px;left:0;width:1200px;display:flex;justify-content:center;gap:60px;color:#fff;font-size:15px;font-weight:600}
.footer-rule{position:absolute;top:368px;left:120px;width:960px;height:1px;background:rgba(255,255,255,.2)}
.footer-contacts{position:absolute;top:392px;left:120px;width:960px;display:flex;justify-content:space-between}
.fc{display:flex;gap:14px;align-items:center;color:#d6d3dc;font-size:13px;width:300px}
.fc .dot{width:44px;height:44px;border-radius:50%;border:1px solid rgba(255,255,255,.4);display:flex;align-items:center;justify-content:center;flex:none}
.fc b{display:block;color:#fff;font-size:14px}
.fc.sep{border-left:1px solid rgba(255,255,255,.2);padding-left:30px}
.footer-bar{position:absolute;bottom:0;left:0;width:1200px;height:60px;background:linear-gradient(90deg,var(--purple),var(--purple-mid));display:flex;align-items:center;justify-content:space-between;padding:0 120px;color:#fff;font-size:14px;font-weight:600}
.socials{display:flex;gap:10px}
.socials span{width:26px;height:26px;border-radius:50%;background:rgba(255,255,255,.25)}
</style>
</head>
<body>

<header class="site-header">
  <div class="contact-chip" style="left:120px">
    <span class="dot"><svg width="16" height="16" viewBox="0 0 24 24" fill="#fff"><path d="M6.6 10.8a15 15 0 006.6 6.6l2.2-2.2c.3-.3.7-.4 1-.2 1.1.4 2.3.6 3.6.6.6 0 1 .4 1 1V20c0 .6-.4 1-1 1A17 17 0 013 4c0-.6.4-1 1-1h3.5c.6 0 1 .4 1 1 0 1.3.2 2.5.6 3.6.1.3 0 .7-.2 1z"/></svg></span>
    <div><b>Call Us</b>(555) 014 2290</div>
  </div>
  <div class="contact-chip" style="left:300px">
    <span class="dot"><svg width="16" height="16" viewBox="0 0 24 24" fill="#fff"><path d="M2 5h20v14H2zm2 2v.4l8 5 8-5V7z"/></svg></span>
    <div><b>Email</b>hello@sungroveyoga.com</div>
  </div>
  <div class="book-btn">BOOK APPOINTMENT</div>
  <nav class="main-nav"><span>Home</span><span>About Us</span><span>Services</span><span class="gap"></span><span>Classes</span><span>Blog</span><span>Contact Us</span></nav>
  <div class="brand-badge"><span class="mark"></span><span class="name">SunGrove Yoga</span></div>
</header>

<section class="hero">
  <div class="hero-photo" role="img" aria-label="Woman seated in a meditation pose by the sea at sunset, arms raised overhead"></div>
  <div class="hero-text">
    <div class="eyebrow">SUNGROVE YOGA</div>
    <h1>Empower Your Life with Yoga</h1>
    <p>Lorem ipsum dolor sit amet, consectetur adipiscing elit, sed do eiusmod tempor incididunt ut labore et dolore magna</p>
    <div class="actions"><span class="btn btn-purple">Learn More</span><span class="btn btn-white">Request Quote</span></div>
  </div>
  <svg class="hero-curve" width="1200" height="200" viewBox="0 0 1200 200">
    <path d="M0 60 Q600 230 1200 40 L1200 200 L0 200Z" fill="#8869af"/>
    <path d="M0 95 Q600 250 1200 75 L1200 200 L0 200Z" fill="#6b429c"/>
    <path d="M0 120 Q600 250 1200 110 L1200 200 L0 200Z" fill="#ffffff"/>
  </svg>
</section>

<section class="intro">
  <div class="brand-art"><span class="mark"></span><span class="name">SunGrove Yoga</span></div>
  <div class="intro-copy">
    <div class="kicker">A Path to Inner Radiance</div>
    <h2>Unwind Your Soul with Yoga</h2>
    <div class="rule"></div>
    <p class="lead">Lorem ipsum dolor sit amet, consectetur adipiscing elit, sed do eiusmod tempor incididunt ut labore et dolore magna aliqua.</p>
    <p>Lorem ipsum dolor sit amet, consectetur adipiscing elit, sed do eiusmod tempor incididunt ut labore et dolore magna. Lorem ipsum dolor sit amet, consectetur adipiscing elit, sed do eiusmod tempor incididunt ut labore et dolore magna aliqua. Ut enim ad minim veniam, quis nostrud exercitation ullamco laboris nisi ut aliquip ex ea commodo consequat.</p>
    <p>Lorem ipsum dolor sit amet, consectetur adipiscing elit, sed do eiusmod tempor incididunt ut labore et dolore magna aliqua.</p>
    <span class="btn btn-purple" style="text-transform:none">Contact us</span>
  </div>
</section>

<section class="benefits">
  <div class="sec-title"><h2>Benefits of Yoga</h2><p>Lorem ipsum dolor sit amet, consectetur adipiscing elit, sed do eiusmod tempor incididunt ut labore et dolore</p></div>
  <div class="benefit-wrap" style="left:92px">
    <div class="benefit-card" role="img" aria-label="Group of people practising yoga in a studio"><h3>Healthy Minds</h3>
      <svg class="benefit-arrow" width="40" height="16" viewBox="0 0 40 16"><path d="M0 8h36M30 2l6 6-6 6" stroke="#fff" stroke-width="2" fill="none"/></svg></div>
    <svg class="benefit-icon" width="52" height="52" viewBox="0 0 52 52"><circle cx="26" cy="26" r="25" fill="#fff"/><circle cx="26" cy="26" r="8" fill="none" stroke="#6b429c" stroke-width="2"/></svg>
  </div>
  <div class="benefit-wrap" style="left:440px">
    <div class="benefit-card" role="img" aria-label="Class seated in meditation on yoga mats"><h3>Healthy Minds</h3>
      <svg class="benefit-arrow" width="40" height="16" viewBox="0 0 40 16"><path d="M0 8h36M30 2l6 6-6 6" stroke="#fff" stroke-width="2" fill="none"/></svg></div>
    <svg class="benefit-icon" width="52" height="52" viewBox="0 0 52 52"><circle cx="26" cy="26" r="25" fill="#fff"/><path d="M18 34l8-16 8 16z" fill="none" stroke="#6b429c" stroke-width="2"/></svg>
  </div>
  <div class="benefit-wrap" style="left:788px">
    <div class="benefit-card" role="img" aria-label="Woman stretching in a bright yoga room"><h3>Healthy Spirits</h3>
      <svg class="benefit-arrow" width="40" height="16" viewBox="0 0 40 16"><path d="M0 8h36M30 2l6 6-6 6" stroke="#fff" stroke-width="2" fill="none"/></svg></div>
    <svg class="benefit-icon" width="52" height="52" viewBox="0 0 52 52"><circle cx="26" cy="26" r="25" fill="#fff"/><circle cx="26" cy="20" r="4" fill="#6b429c"/><path d="M16 34h20" stroke="#6b429c" stroke-width="2"/></svg>
  </div>
</section>

<section class="why">
  <div class="sec-title"><h2>Why Choose Us</h2><p>Lorem ipsum dolor sit amet, consectetur adipiscing elit, sed do eiusmod temp or incididunt ut labore et dolore</p></div>
  <div class="why-glow"></div>
  <div class="why-photo" role="img" aria-label="Woman in white sportswear seated cross-legged in meditation"></div>

  <div class="feature left" style="left:70px;top:280px"><h4>Variety of Classes</h4><p>Lorem ipsum dolor sit amet, consectetur adipiscing elit, sed do eiusmod tempor incididunt ut labore</p></div>
  <div class="feature left" style="left:50px;top:405px"><h4>Certified Instructors</h4><p>Lorem ipsum dolor sit amet, consectetur adipiscing elit, sed do eiusmod tempor incididunt ut labore</p></div>
  <div class="feature left" style="left:70px;top:530px"><h4>Personalized Approach</h4><p>Lorem ipsum dolor sit amet, consectetur adipiscing elit, sed do eiusmod tempor incididunt ut labore</p></div>
  <div class="f-icon" style="left:352px;top:284px"></div>
  <div class="f-icon" style="left:332px;top:408px"></div>
  <div class="f-icon" style="left:352px;top:532px"></div>

  <div class="feature" style="left:870px;top:280px"><h4>Mind-Body Connection</h4><p>Lorem ipsum dolor sit amet, consectetur adipiscing elit, sed do eiusmod tempor incididunt ut labore</p></div>
  <div class="feature" style="left:890px;top:405px"><h4>Flexible Schedule</h4><p>Lorem ipsum dolor sit amet, consectetur adipiscing elit, sed do eiusmod tempor incididunt ut labore</p></div>
  <div class="feature" style="left:870px;top:530px"><h4>Specialized Workshops</h4><p>Lorem ipsum dolor sit amet, consectetur adipiscing elit, sed do eiusmod tempor incididunt ut labore</p></div>
  <div class="f-icon" style="left:774px;top:284px"></div>
  <div class="f-icon" style="left:794px;top:408px"></div>
  <div class="f-icon" style="left:774px;top:532px"></div>
</section>

<section class="hours">
  <div class="hours-photo" role="img" aria-label="Dim yoga studio with people stretching on mats"></div>
  <div class="hours-title">Opening Hours of SunGrove yoga</div>
  <div class="hours-table">
    <div class="hours-row"><span>Monday - Thursday</span><span>08am - 05pm</span></div>
    <div class="hours-row"><span>Saturday</span><span>08am - 02pm</span></div>
    <div class="hours-row"><span>Phone</span><span>(555) 014 2290</span></div>
    <div class="hours-row" style="border:0"><span>Email</span><span>hello@sungroveyoga.com</span></div>
  </div>
  <div class="appt">
    <div class="appt-head">
      <span class="dot"><svg width="20" height="20" viewBox="0 0 24 24" fill="#fff"><path d="M6.6 10.8a15 15 0 006.6 6.6l2.2-2.2c.3-.3.7-.4 1-.2 1.1.4 2.3.6 3.6.6.6 0 1 .4 1 1V20c0 .6-.4 1-1 1A17 17 0 013 4c0-.6.4-1 1-1h3.5c.6 0 1 .4 1 1 0 1.3.2 2.5.6 3.6.1.3 0 .7-.2 1z"/></svg></span>
      <div><small>Get in touch with us any day any time</small><h3>Make Appointment</h3></div>
    </div>
    <div class="fields">
      <div class="field">First Name</div><div class="field">Last Name</div>
      <div class="field">Email Address</div><div class="field">Phone Number</div>
      <div class="field full">Select Subject</div>
      <div class="field full">dd/mm/yyyy</div>
      <div class="submit">SUBMIT</div>
    </div>
  </div>
</section>

<section class="reviews">
  <div class="sec-title"><h2>Clients Review</h2><p>Lorem ipsum dolor sit amet, consectetur adipiscing elit, sed do eiusmod temp or incididunt ut labore et dolore</p></div>
  <div class="review" style="left:100px"><div class="avatar" role="img" aria-label="Client portrait"></div><div class="quote">&#8221;</div><div class="stars">★★★★★</div><p>Lorem ipsum dolor sit amet, consectetur adipiscing elit, sed do eiusmod tempor incididunt ut labore et dolore magna aliqua. Ut enim ad minim.</p><h5>Mira Lenholt</h5><small>Accountant</small></div>
  <div class="review" style="left:440px"><div class="avatar" role="img" aria-label="Client portrait"></div><div class="quote">&#8221;</div><div class="stars">★★★★★</div><p>Lorem ipsum dolor sit amet, consectetur adipiscing elit, sed do eiusmod tempor incididunt ut labore et dolore magna aliqua. Ut enim ad minim.</p><h5>Mira Lenholt</h5><small>Accountant</small></div>
  <div class="review" style="left:780px"><div class="avatar" role="img" aria-label="Client portrait"></div><div class="quote">&#8221;</div><div class="stars">★★★★★</div><p>Lorem ipsum dolor sit amet, consectetur adipiscing elit, sed do eiusmod tempor incididunt ut labore et dolore magna aliqua. Ut enim ad minim.</p><h5>Mira Lenholt</h5><small>Accountant</small></div>
</section>

<footer class="site-footer">
  <svg class="footer-curve" width="1200" height="90" viewBox="0 0 1200 90">
    <path d="M0 0 H1200 V20 Q600 110 0 20Z" fill="#ffffff"/>
    <path d="M0 20 Q600 110 1200 20 L1200 28 Q600 118 0 28Z" fill="#8869af"/>
  </svg>
  <div class="footer-brand"><span class="mark"></span><span class="name">SunGrove Yoga</span></div>
  <nav class="footer-nav"><span>HOME</span><span>SERVICES</span><span>ABOUT US</span><span>TESTIMONIALS</span><span>BLOG</span></nav>
  <div class="footer-rule"></div>
  <div class="footer-contacts">
    <div class="fc"><span class="dot"><svg width="18" height="18" viewBox="0 0 24 24" fill="#fff"><path d="M12 2a7 7 0 00-7 7c0 5 7 13 7 13s7-8 7-13a7 7 0 00-7-7zm0 9.5A2.5 2.5 0 1112 6a2.5 2.5 0 010 5.5z"/></svg></span><div>48 Orchard Lane,<br>Fernvale, CA 90210</div></div>
    <div class="fc sep"><span class="dot"><svg width="18" height="18" viewBox="0 0 24 24" fill="#fff"><path d="M6.6 10.8a15 15 0 006.6 6.6l2.2-2.2c.3-.3.7-.4 1-.2 1.1.4 2.3.6 3.6.6.6 0 1 .4 1 1V20c0 .6-.4 1-1 1A17 17 0 013 4c0-.6.4-1 1-1h3.5c.6 0 1 .4 1 1 0 1.3.2 2.5.6 3.6.1.3 0 .7-.2 1z"/></svg></span><div><b>PHONE</b>(555) 014 2290</div></div>
    <div class="fc sep"><span class="dot"><svg width="18" height="18" viewBox="0 0 24 24" fill="#fff"><path d="M2 5h20v14H2zm2 2v.4l8 5 8-5V7z"/></svg></span><div><b>EMAIL</b>hello@sungroveyoga.com</div></div>
  </div>
  <div class="footer-bar"><span>SunGrove Yoga</span><div class="socials"><span></span><span></span><span></span><span></span></div></div>
</footer>

</body>
</html>
```